Author book launch promotion design for social media

We are organising an authors book launch event and require an author promotion design that will be used on social media (Chatterbook, netted) promotion.

The design must have the author's photo, image of their book, the event logo, details of the event plus website address (penfairhall.com.au).

Details of the event can be found at penfairhall.com.au.

the design has to be attractive and inviting and colours in accordance with the brand colours.

You can choose 1 one of the book images attached
Author name: Dr Tarek Bismil
Event Details
LAUNCH YOUR BOOK IN STYLE

Quillmark Reading Fair and Showcase 2022
7 - 8 October 2022
Melbourne Larkvale Centre
14 Corrigal St, Southbank Melbourne

For registration and ticketing visit:
penfairhall.com.au

I have attached also a sample promo. Please be creative.

```html
<!DOCTYPE html>
<html lang="en">
<head>
<meta charset="utf-8">
<title>Quillmark Reading Fair and Showcase 2022 – Dr Tarek Bismil</title>
<link rel="stylesheet" href="https://fonts.googleapis.com/css2?family=Poppins:ital,wght@0,400;0,600;0,700;1,700&display=swap">
<style>
  :root {
    --ink: #0b1418;
    --teal-deep: #10252b;
    --teal-mid: #1c3a42;
    --rose: #c52a5c;
    --gold: #d9a04a;
    --gold-light: #e6b766;
    --white: #ffffff;
    --cover-grey: #e4e4e4;
  }
  * { margin: 0; padding: 0; box-sizing: border-box; }
  html, body { width: 1200px; height: 1200px; overflow: hidden; background: var(--ink); }
  .promo {
    position: relative;
    width: 1200px;
    height: 1200px;
    overflow: hidden;
    font-family: "Poppins", sans-serif;
    color: var(--white);
    background:
      radial-gradient(ellipse at 35% 45%, var(--teal-mid) 0%, transparent 55%),
      radial-gradient(ellipse at 80% 20%, #16313a 0%, transparent 50%),
      var(--ink);
  }
  .event-ribbon {
    position: absolute; left: 63px; top: 0; width: 332px; height: 326px;
  }
  .event-mark {
    position: absolute; left: 63px; top: 110px; width: 332px;
    display: flex; align-items: center; justify-content: center; gap: 12px;
    font-weight: 700; font-size: 44px; color: var(--gold-light); letter-spacing: 1px;
  }
  .event-mark__dot { width: 22px; height: 22px; border-radius: 50%; background: var(--gold-light); }
  .launch-banner { position: absolute; left: 500px; top: 0; width: 700px; height: 205px; }
  .launch-banner__title {
    position: absolute; left: 555px; top: 22px;
    font-weight: 600; font-size: 92px; line-height: 1; letter-spacing: 2px;
  }
  .launch-banner__sub {
    position: absolute; left: 556px; top: 124px;
    font-weight: 600; font-size: 50px; line-height: 1; color: var(--rose);
  }
  .event-title { position: absolute; left: 68px; top: 395px; font-weight: 600; line-height: 1.05; }
  .event-title__lead { display: block; font-size: 56px; }
  .event-title__accent { display: block; font-size: 46px; color: var(--gold); }
  .event-title__tail { display: block; font-size: 46px; }
  .event-date { position: absolute; left: 68px; top: 620px; font-weight: 600; }
  .event-date__days { font-size: 40px; line-height: 1; }
  .event-date__days small { font-size: 28px; }
  .event-date__year { display: block; font-size: 68px; line-height: 1.1; margin-left: -6px; }
  .event-divider { position: absolute; left: 246px; top: 625px; width: 2px; height: 133px; background: var(--gold); }
  .event-venue { position: absolute; left: 278px; top: 626px; font-size: 26px; line-height: 32.5px; font-weight: 400; }
  .author-strip {
    position: absolute; left: 0; top: 808px; width: 607px; height: 130px;
    background: linear-gradient(90deg, #0f2a30 0%, #1f4a52 50%, #173940 100%);
    border-right: 3px solid rgba(255,255,255,0.6);
  }
  .author-strip__label {
    position: absolute; left: 68px; top: 824px; font-size: 30px; color: var(--rose); font-weight: 400;
  }
  .author-strip__name {
    position: absolute; left: 58px; top: 858px; font-size: 54px; font-weight: 700; font-style: italic; line-height: 1;
  }
  .ticket-panel { position: absolute; left: 0; top: 948px; width: 640px; height: 252px; }
  .ticket-icon { position: absolute; left: 205px; top: 990px; width: 80px; height: 80px; }
  .ticket-panel__note {
    position: absolute; left: 44px; top: 1085px; font-size: 27px; font-weight: 600; color: var(--gold);
  }
  .ticket-panel__site {
    position: absolute; left: 44px; top: 1118px; font-size: 42px; font-weight: 600; line-height: 1.1;
  }
  .book-cover {
    position: absolute; left: 604px; top: 262px; width: 566px; height: 898px;
    background: linear-gradient(90deg, var(--rose) 0%, var(--rose) 9%, #f2f2f2 10%, var(--cover-grey) 60%, #bfbfbf 100%);
    box-shadow: 0 20px 40px rgba(0,0,0,0.5);
    border-radius: 2px 6px 6px 2px;
  }
</style>
</head>
<body>
<main class="promo">
  <svg class="event-ribbon" viewBox="0 0 332 326" aria-hidden="true">
    <polygon points="0,0 332,0 332,326 166,264 0,326" fill="var(--rose)"/>
  </svg>
  <div class="event-mark"><span class="event-mark__dot"></span>QUILLMARK</div>

  <svg class="launch-banner" viewBox="0 0 700 205" aria-hidden="true">
    <polygon points="0,0 700,0 700,40 625,205 30,205 0,0" fill="var(--gold)"/>
  </svg>
  <div class="launch-banner__title">LAUNCH</div>
  <div class="launch-banner__sub">YOUR BOOK IN STYLE</div>

  <h1 class="event-title">
    <span class="event-title__lead">Quillmark Reading</span>
    <span class="event-title__accent">Fair and</span>
    <span class="event-title__tail">Showcase 2022</span>
  </h1>

  <div class="event-date">
    <span class="event-date__days">7 – 8 <small>Oct</small></span>
    <span class="event-date__year">2022</span>
  </div>
  <div class="event-divider"></div>
  <address class="event-venue" style="font-style:normal">
    Melbourne Larkvale<br>Centre<br>14 Corrigal St,<br>Southbank Melbourne
  </address>

  <div class="author-strip"></div>
  <div class="author-strip__label">AUTHOR NAME</div>
  <div class="author-strip__name">Dr Tarek Bismil</div>

  <svg class="ticket-panel" viewBox="0 0 640 252" aria-hidden="true">
    <circle cx="245" cy="82" r="80" fill="var(--rose)"/>
    <polygon points="0,92 530,92 600,252 0,252" fill="var(--rose)"/>
  </svg>
  <svg class="ticket-icon" viewBox="0 0 80 80" aria-hidden="true" fill="none" stroke="var(--white)" stroke-width="3" stroke-linejoin="round">
    <path d="M10 48 L44 14 L52 22 A6 6 0 0 0 60 30 L68 38 L34 72 L26 64 A6 6 0 0 0 18 56 Z"/>
    <path d="M34 36 L48 50 M30 42 L42 54 M38 30 L52 44" stroke-width="2.5"/>
  </svg>
  <div class="ticket-panel__note">For registration and ticketing visit:</div>
  <div class="ticket-panel__site">penfairhall.com.au</div>

  <div class="book-cover" role="img" aria-label="Book cover mock-up of the author's new title with author portrait"></div>
</main>
</body>
</html>
```